依頼詳細
【概要】昨年度、会社を設立しまして、今年度名刺交換をする機会が非常に多くなってきたので、名刺作成の依頼を希望しています。
ひとまず、代表取締役、私一人分の名刺作成を考えております。

特記事項:代表取締役ですが、私自身が営業に
出向くこともあり、代表取締役の肩書だけだと
営業しにくい事もあり、
代表取締役と
営業部 コンサルティング部門  課長
の肩書を別々の名刺に
二通りの作成お願いしたいです。
記載項目
株式会社 RTW

エステティック関連事業

代表取締役
森下 健吾

会社住所
〒630-8472 奈良市柳原町5丁目1番7-308

TEL 0742-69-2035
MOBILE 080-5927-1364
希望イメージ
シンプル 複雑
単色 カラフル
暗い 明るい
日常 高級
遊び心 厳粛
未来的 伝統的
女性的 男性的
希望する色
黄・オレンジ系、茶系、無彩色系
納品ファイル
• イラストレーター形式 (.ai)
補足説明
サイズ:通常名刺サイズ 91×55mm(横向き)名刺に記載する内容:(表)株式会社RTWかRTWの文字だけでもいいと考えております。拾い画像ですが、下記の添付ファイルのような名刺デザインが良いと考えております。
■ 選んだ理由

RTWの社名が短いので、名刺交換の時に印象が残りづらいという懸念が依頼当初
あったのですが、選ばせて頂いた作品は、RTWの文字自体のデザインが非常に工夫されていて、なおかつ分かり易く、色使いも人目を惹きつけるものがあるので決めさせて頂きました。
私のイメージしていたものを遥かに超える作品だったのも理由の一つです。

■ 提案者全員のお礼・コメント

私自身、毎日皆様からの作品を見せて頂くことが楽しみの一つとなっておりました。

こんなにも、多くのデザイナー様から案を頂くことができ、コンペに

ご依頼してよかったと思っております。

最後にはなりましたが、たくさんのご提案、誠にありがとうございました。

```html
<!DOCTYPE html>
<html lang="ja">
<head>
<meta charset="utf-8">
<title>株式会社RTW 名刺デザイン</title>
<link rel="stylesheet" href="https://fonts.googleapis.com/css2?family=Cormorant+Garamond:wght@500&family=Noto+Serif+JP:wght@400;500&display=swap">
<style>
  :root {
    --sheet: #ffffff;
    --sheet-edge: #cfcfcf;
    --card: #4a4746;
    --accent: #dd7442;
    --ink: #f1eeea;
    --ink-soft: #d6d1cc;
  }
  * { margin: 0; padding: 0; box-sizing: border-box; }
  html, body {
    width: 888px;
    height: 1200px;
    overflow: hidden;
    background: var(--sheet);
  }
  .sheet {
    position: relative;
    width: 888px;
    height: 1200px;
    border: 2px solid var(--sheet-edge);
    background: var(--sheet);
    font-family: "Noto Serif JP", serif;
  }
  .card {
    position: absolute;
    left: 57px;
    width: 776px;
    height: 489px;
    background: var(--card);
    overflow: hidden;
  }
  .card--front { top: 57px; }
  .card--back  { top: 620px; }

  /* front */
  .front-logo {
    position: absolute;
    left: 600px;
    top: 58px;
    width: 120px;
    text-align: center;
    color: var(--accent);
  }
  .front-logo__kind {
    display: block;
    font-size: 11px;
    letter-spacing: 0.15em;
    line-height: 1;
  }
  .front-logo__name {
    display: block;
    font-family: "Cormorant Garamond", serif;
    font-weight: 500;
    font-size: 46px;
    line-height: 1;
    margin-top: 6px;
  }
  .person {
    position: absolute;
    left: 556px;
    top: 198px;
    width: 190px;
    color: var(--ink);
  }
  .person__title {
    font-size: 15px;
    letter-spacing: 0.12em;
    text-align: right;
    padding-right: 60px;
  }
  .person__name {
    font-size: 34px;
    font-weight: 500;
    letter-spacing: 0.18em;
    margin-top: 6px;
    line-height: 1.2;
  }
  .person__roman {
    font-family: "Cormorant Garamond", serif;
    font-size: 15px;
    letter-spacing: 0.05em;
    margin-top: 4px;
    padding-left: 12px;
  }
  .company {
    position: absolute;
    left: 541px;
    top: 332px;
    width: 220px;
    color: var(--ink-soft);
  }
  .company__name {
    font-size: 15px;
    letter-spacing: 0.06em;
    color: var(--ink);
  }
  .company__field {
    font-size: 12px;
    margin-top: 2px;
    letter-spacing: 0.04em;
  }
  .company__contact {
    list-style: none;
    margin-top: 8px;
    font-size: 10.5px;
    line-height: 18px;
    letter-spacing: 0.03em;
  }

  /* back */
  .back-kind {
    position: absolute;
    left: 168px;
    top: 262px;
    font-size: 27px;
    letter-spacing: 0.12em;
    color: var(--accent);
  }
  .back-mark {
    position: absolute;
    left: -6px;
    bottom: -34px;
    font-family: "Cormorant Garamond", serif;
    font-weight: 500;
    font-size: 236px;
    line-height: 1;
    letter-spacing: -0.03em;
    color: var(--accent);
  }
</style>
</head>
<body>
  <main class="sheet">
    <section class="card card--front" aria-label="名刺 表面">
      <div class="front-logo">
        <span class="front-logo__kind">株式会社</span>
        <span class="front-logo__name">RTW</span>
      </div>
      <div class="person">
        <p class="person__title">代表取締役</p>
        <p class="person__name">森下 健吾</p>
        <p class="person__roman">Morishita Kengo</p>
      </div>
      <div class="company">
        <p class="company__name">株式会社 RTW</p>
        <p class="company__field">エステティック関連事業</p>
        <ul class="company__contact">
          <li>〒630-8472</li>
          <li>奈良市柳原町5丁目1番7-308</li>
          <li>tel 0742-69-2035</li>
          <li>mobile 080-5927-1364</li>
          <li>morishita.k@rtw-nara.jp</li>
        </ul>
      </div>
    </section>

    <section class="card card--back" aria-label="名刺 裏面">
      <p class="back-kind">株式会社</p>
      <p class="back-mark">RTW</p>
    </section>
  </main>
</body>
</html>
```